Marina Web Page

I'm looking for a visually engaging web page/layout that I can use as the basis for a website for my Marina. I need to include page content that can be stored and updated in an include file to allow someone to easily manage content without editing html or needing to understand html.

The business is a small marina and fishing center located on the Pamlico sound in eastern North Carolina right off the Intracoastal Waterway. We offer wet slips with power, water, and wifi and also have powered RV slips for camping available. The Marina sells fuel, beer, tackle/bait, and ice. The Marina also has an island style bar (The Gullwing Bar) and live music most weekends. The bar has a mascot named Tazzo, short for captain, who is a black labradoodle know for diving to the bottom of the marina basin to retrieve oysters and rocks. Tazzo could be incorporated as a minor design element but isn't a requirement.The marina caters to coastal sportsmen interested in sound fishing as well as offshore sport fishing. The Marina also offers fishing charters form a 32' Wavecrest fishing boat w/ tuna tower.

The primary purpose of the initial version of the website is to communicate information about up coming events, music, bar specials etc... It will also be used to feature our services, fishing report and weather info, where we are located from both land and water, and a photo gallery.

Target Market(s)

Coastal sports enthusiast and the coastal boating community

Industry/Entity Type

Business

Requirements
Must have
• I would like animated menus incorporated into the page temple. It must also allow for the updating/storing of page content in a separate file to that an employee of the marina can update specials and events without having to understand or edit html.
Nice to have
• A photo gallery option that will present photos from a folder on the web server. Changing photos should be as easy as adding or deleting photos from the folder.

```html
<!DOCTYPE html>
<html lang="en">
<head>
<meta charset="utf-8">
<title>Harbor Reach Marina</title>
<link rel="stylesheet" href="https://fonts.googleapis.com/css2?family=Source+Sans+3:wght@400;600;700&family=Comfortaa:wght@500;700&display=swap">
<style>
:root{
  --night:#1b1b1b;
  --paper:#efefef;
  --ink:#333333;
  --ink-soft:#555555;
  --blue:#3d95dd;
  --blue-deep:#1a66b4;
  --blue-light:#5fb6ee;
  --navy:#24509a;
  --rule:#9a9a9a;
  --white:#ffffff;
  --tile-1:#3a5a98;
  --tile-2:#4cc0ee;
  --tile-3:#2b7db3;
  --tile-4:#3a3a3a;
  --tile-5:#c4302b;
}
*{box-sizing:border-box;margin:0;padding:0}
html,body{width:1037px;height:1200px;overflow:hidden}
body{
  position:relative;
  font-family:"Source Sans 3",sans-serif;
  color:var(--ink);
  background:linear-gradient(180deg,#e2e2e2 370px,var(--paper) 520px);
}
.header-band{
  position:absolute;left:0;top:0;width:1037px;height:370px;
  background:repeating-linear-gradient(0deg,var(--night) 0 2px,#232323 2px 4px);
}
.brand{
  position:absolute;left:160px;top:58px;
  display:flex;align-items:center;gap:10px;
}
.brand-mark{width:22px;height:22px;border-radius:50%;background:var(--blue)}
.brand-name{font-size:29px;font-weight:700;color:var(--white);letter-spacing:.3px}
.phone-tab{
  position:absolute;left:758px;top:0;width:182px;height:49px;
  background:linear-gradient(180deg,var(--blue-light),var(--blue-deep));
  border-radius:0 0 4px 4px;
  display:flex;align-items:center;gap:10px;padding-left:12px;
  color:var(--white);font-size:15px;
}
.phone-tab .icon{
  width:34px;height:34px;border-radius:6px;background:var(--blue-deep);
  display:flex;align-items:center;justify-content:center;
}
.main-nav{
  position:absolute;left:444px;top:111px;display:flex;align-items:center;
  font-size:13px;color:var(--white);
}
.main-nav a{color:inherit;text-decoration:none;padding:0 7.5px;line-height:36px}
.main-nav a.is-active{
  background:linear-gradient(180deg,var(--blue-light),var(--blue-deep));
  border:1px solid #7cc6f4;border-radius:6px;padding:0 14px;margin-right:4px;
}
.slider{
  position:absolute;left:105px;top:159px;width:833px;height:338px;
  background:var(--blue);border-radius:8px;padding:8px 10px 11px 9px;
  box-shadow:0 18px 40px rgba(0,0,0,.35);
}
.slider-photo{
  position:relative;width:100%;height:100%;overflow:hidden;
  background:
    radial-gradient(ellipse 32% 28% at 88% 50%,rgba(235,240,244,.9),rgba(235,240,244,0)),
    radial-gradient(ellipse 40% 22% at 55% 88%,rgba(225,232,236,.85),rgba(225,232,236,0)),
    radial-gradient(ellipse 30% 30% at 58% 45%,rgba(210,214,214,.55),rgba(210,214,214,0)),
    linear-gradient(180deg,#33464f 0%,#3c5560 45%,#4f6873 75%,#8ea3ad 100%);
}
.slider-arrow{
  position:absolute;top:136px;width:53px;height:55px;
  background:rgba(80,80,80,.6);display:flex;align-items:center;justify-content:center;
}
.slider-arrow.prev{left:0}
.slider-arrow.next{right:0}
.slider-caption{
  position:absolute;right:34px;bottom:20px;
  font-family:"Comfortaa",sans-serif;font-weight:500;font-size:17.5px;color:var(--white);
  text-shadow:0 0 3px #0a4a7a,0 0 2px #0a4a7a,0 0 1px #0a4a7a;
}
.welcome{position:absolute;left:117px;top:525px;width:528px}
.section-title{
  font-size:20.5px;font-weight:400;color:var(--ink);
  padding-bottom:3px;border-bottom:1px solid var(--rule);
}
.section-title span{color:var(--navy)}
.welcome .section-title{width:445px}
.lead{font-size:11.5px;margin-top:8px;color:#222;font-weight:400}
.body-copy{font-size:9.5px;line-height:15.5px;color:var(--ink-soft);margin-top:9px}
.btn-read{
  position:absolute;left:458px;top:157px;width:70px;height:28px;
  background:linear-gradient(180deg,#9fd3f6,#5fb2ec);
  font-size:11.5px;font-weight:600;color:#123;display:flex;align-items:center;justify-content:center;
}
.gallery{position:absolute;left:116px;top:754px;width:530px}
.gallery .section-title{width:513px}
.gallery-arrows{position:absolute;right:18px;top:8px;display:flex;gap:8px}
.gallery-photo{position:absolute;border:2px solid #d8d8d8;box-shadow:0 1px 3px rgba(0,0,0,.2)}
.gallery-photo.is-current{border-color:var(--blue-light)}
.gallery-caption{position:absolute;left:1px;top:246px;width:520px}
.promo{
  position:absolute;left:700px;top:542px;width:236px;height:210px;
  border:2px solid #ddd;border-radius:6px;overflow:hidden;
  background:
    linear-gradient(90deg,rgba(0,0,0,0) 78%,rgba(90,80,70,.55) 85%,rgba(130,120,105,.6) 100%),
    radial-gradient(ellipse 45% 12% at 45% 46%,rgba(250,250,250,.95),rgba(250,250,250,0)),
    linear-gradient(180deg,#a9bfd6 0%,#b9a89a 14%,#c9d4dc 26%,#aebdc8 40%,#dfe4e6 50%,#8b9aa2 65%,#4a5860 100%);
}
.promo-text{
  position:absolute;left:20px;top:136px;font-size:21.5px;line-height:28px;color:var(--white);
  text-shadow:0 1px 3px rgba(0,0,0,.6);
}
.newsletter{
  position:absolute;left:701px;top:783px;width:232px;height:223px;
  background:var(--white);border:2px solid #d6d6d6;border-radius:4px;padding:12px 17px;
}
.newsletter h3{
  display:flex;align-items:center;gap:9px;font-size:17.5px;font-weight:400;
  border-bottom:1px solid var(--rule);padding-bottom:4px;margin:0 -2px 0 -8px;
}
.newsletter p{font-size:9.5px;line-height:15.5px;color:var(--ink-soft);margin-top:7px}
.field{
  display:block;width:200px;height:24px;margin:11px 0 0 -6px;border:1px solid #ccc;
  font-size:9.5px;color:#666;padding:5px 8px;font-family:inherit;background:var(--white);
}
.btn-subscribe{
  position:absolute;right:20px;top:170px;width:94px;height:29px;border-radius:8px;
  background:linear-gradient(180deg,var(--blue-light),var(--blue-deep));
  color:var(--white);font-size:14px;font-weight:700;display:flex;align-items:center;justify-content:center;
}
.site-footer{
  position:absolute;left:0;top:1089px;width:1037px;height:111px;
  background:linear-gradient(180deg,#3a9ae0,#2f86cf 45%,#1c6ab8);
}
.social{position:absolute;left:111px;top:29px;display:flex;gap:12px}
.social-tile{
  width:23px;height:23px;border-radius:2px;
  box-shadow:0 1px 2px rgba(0,0,0,.35),inset 0 1px 0 rgba(255,255,255,.3);
}
.social-tile.t1{background:var(--tile-1)}
.social-tile.t2{background:var(--tile-2)}
.social-tile.t3{background:var(--tile-3)}
.social-tile.t4{background:var(--tile-4)}
.social-tile.t5{background:var(--tile-5)}
.copyright{position:absolute;right:101px;top:20px;font-size:10.8px;color:var(--white)}
</style>
</head>
<body>
<div class="header-band"></div>

<div class="brand">
  <span class="brand-mark"></span>
  <span class="brand-name">Harbor Reach Marina</span>
</div>

<div class="phone-tab">
  <span class="icon">
    <svg width="20" height="20" viewBox="0 0 24 24"><path fill="#fff" d="M6.6 10.8a15 15 0 0 0 6.6 6.6l2.2-2.2c.3-.3.7-.4 1-.2 1.1.4 2.3.6 3.6.6.6 0 1 .4 1 1V20c0 .6-.4 1-1 1A17 17 0 0 1 3 4c0-.6.4-1 1-1h3.5c.6 0 1 .4 1 1 0 1.3.2 2.5.6 3.6.1.3 0 .7-.2 1z"/></svg>
  </span>
  +1 252 555 0148
</div>

<nav class="main-nav">
  <a class="is-active" href="#">Home</a>
  <a href="#">About Us</a>
  <a href="#">Services</a>
  <a href="#">Slips</a>
  <a href="#">Boat Info</a>
  <a href="#">Testimonials</a>
  <a href="#">Contact</a>
</nav>

<section class="slider">
  <div class="slider-photo" role="img" aria-label="Sport fishing boat with tuna tower running across open water">
    <div class="slider-arrow prev"><svg width="14" height="22" viewBox="0 0 14 22"><path d="M11 2 3 11l8 9" fill="none" stroke="#bbb" stroke-width="3"/></svg></div>
    <div class="slider-arrow next"><svg width="14" height="22" viewBox="0 0 14 22"><path d="m3 2 8 9-8 9" fill="none" stroke="#ddd" stroke-width="3"/></svg></div>
    <p class="slider-caption">Our business is a small marina and fishing center</p>
  </div>
</section>

<section class="welcome">
  <h2 class="section-title">Welcome to&nbsp; Harbor Reach <span>Marina</span></h2>
  <p class="lead">Mauris vel lacus vitae felis vestibulum volutpat. Etiam est nunc, venisl.</p>
  <p class="body-copy">Sed ut perspiciatis unde omnis iste natus error sit voluptatem accusantium doloremque laudantium, totam rem aperiam, eaque ipsa quae ab illo inventore veritatis et quasi architecto beatae vitae dicta sunt explicabo. Nemo enim ipsam voluptatem quia voluptas sit aspernatur aut odit aut fugit, sed quia consequuntur magni dolores eos qui ratione voluptatem sequi nesciunt. Neque porro quisquam est, qui dolorem ipsum quia dolor sit amet. Nemo enim ipsam voluptatem quia voluptas sit aspernatur aut odit aut fugit, sed quia consequuntur magni dolores eos qui ratione voluptatem sequi nesciunt. Neque porro quisquam est, qui dolorem ipsum quia dolor sit amet.</p>
  <a class="btn-read">Read More</a>
</section>

<section class="gallery">
  <h2 class="section-title">Photo <span>Gallery</span></h2>
  <div class="gallery-arrows">
    <svg width="10" height="16" viewBox="0 0 10 16"><path d="M8 2 2 8l6 6" fill="none" stroke="#24509a" stroke-width="2"/></svg>
    <svg width="10" height="16" viewBox="0 0 10 16"><path d="m2 2 6 6-6 6" fill="none" stroke="#24509a" stroke-width="2"/></svg>
  </div>
  <div class="gallery-photo is-current" role="img" aria-label="Blue marina building on pilings with a boat at the dock" style="left:-4px;top:48px;width:321px;height:187px;background:radial-gradient(ellipse 22% 14% at 55% 88%,rgba(245,245,245,.9),rgba(245,245,245,0)),linear-gradient(180deg,#4f7fb5 0%,#7f9fbf 12%,#9fb3c4 30%,#8fa6b8 50%,#6b5d50 70%,#4a4540 85%,#5d6a6e 100%)"></div>
  <div class="gallery-photo is-current" role="img" aria-label="Marina building thumbnail" style="left:329px;top:49px;width:91px;height:81px;background:linear-gradient(180deg,#5c87b8 0%,#9aaebf 35%,#6e6255 70%,#b9c2c8 100%)"></div>
  <div class="gallery-photo" role="img" aria-label="Quiet marina basin thumbnail" style="left:433px;top:49px;width:89px;height:81px;background:linear-gradient(180deg,#8d8e84 0%,#5a5a4c 30%,#56646a 55%,#6b7a80 100%)"></div>
  <div class="gallery-photo" role="img" aria-label="Marina dog on the grass thumbnail" style="left:329px;top:150px;width:91px;height:81px;background:radial-gradient(ellipse 40% 45% at 50% 45%,#2b2a27,rgba(43,42,39,0)),linear-gradient(180deg,#6e8f3a,#4f6d2a)"></div>
  <div class="gallery-photo" role="img" aria-label="Guests aboard a boat thumbnail" style="left:433px;top:150px;width:89px;height:81px;background:linear-gradient(180deg,#d6dbd2 0%,#b4b8ac 25%,#6c5a4f 55%,#4b3f38 80%,#7d7068 100%)"></div>
  <p class="body-copy gallery-caption">Sed ut perspiciatis unde omnis iste natus error sit voluptatem accusantium doloremque laudantium, totam rem aperiam, eaque ipsa quae ab illo inventore veritatis et quasi architecto beatae vitae dicta sunt explicabo. Nemo enim ipsam voluptatem quia voluptas sit aspernatur aut odit aut fugit, sed quia consequuntur magni dolores eos qui ratione voluptatem sequi nesciunt.</p>
</section>

<aside class="promo" role="img" aria-label="Boat moored at a wooden dock in front of waterfront buildings">
  <p class="promo-text">We&nbsp; Offer&nbsp; Wet&nbsp; Slips<br>With Power</p>
</aside>

<aside class="newsletter">
  <h3>
    <svg width="19" height="13" viewBox="0 0 19 13"><rect x="1" y="1" width="17" height="11" fill="none" stroke="#333" stroke-width="1.5"/><path d="m1 1 8.5 6L18 1" fill="none" stroke="#333" stroke-width="1.5"/></svg>
    Newsletter
  </h3>
  <p>Uenim ad minim veniam, quis nostrud nisi laboris utaliquip ex irurdolor into</p>
  <input class="field" type="text" placeholder="Name">
  <input class="field" type="email" placeholder="Email" style="margin-left:-5px">
  <a class="btn-subscribe">Subscribe</a>
</aside>

<footer class="site-footer">
  <div class="social" aria-label="Social links">
    <span class="social-tile t1"></span>
    <span class="social-tile t2"></span>
    <span class="social-tile t3"></span>
    <span class="social-tile t4"></span>
    <span class="social-tile t5"></span>
  </div>
  <p class="copyright">© 2013 Harbor Reach Marina., All Rights Reserved</p>
</footer>
</body>
</html>
```